Verdo Studios Business Card

Business card for video production company, I want to give the impression of quality, It has to stand out for its design; it has to be easily readable and please avoid any extravaganza!. I'm looking for a first impression, then the card goes to the trash.

You guys have complete freedom of design! background color, logo colors etc
you can choose one side card or two sided, die cut also a possibility .
Just let me know for what kind of card is your design.
In the files you will find the logo .ai to modify it.

One of the differences between the ambiguous terms Filmmaker and videographer is that filmmaking is more arty, we tend to leave backgrounds out of focus, we create different layers or points of attention with our lens.

Logo
Filmmaking Done Right
www.verdostudios-example.com
www.facebook.com/verdostudios-example
tomas@verdostudios-example.com
555-318-6092
Add QR Code

```html
<!DOCTYPE html>
<html lang="en">
<head>
<meta charset="utf-8">
<title>Verdo Studios Business Card</title>
<link rel="stylesheet" href="https://fonts.googleapis.com/css2?family=Open+Sans:wght@400;600;800&display=swap">
<style>
  :root {
    --backdrop: #d9d7d8;
    --card-front: #060606;
    --card-back: #262424;
    --ink-light: #ffffff;
    --ink-silver: #d6d6d6;
    --accent-red: #e3242b;
    --reel-dark: #111111;
    --reel-mid: #5a5a5a;
    --reel-light: #bdbdbd;
  }
  * { box-sizing: border-box; margin: 0; padding: 0; }
  html, body {
    width: 1200px;
    height: 900px;
    overflow: hidden;
    background: var(--backdrop);
    font-family: "Open Sans", Arial, sans-serif;
  }
  .stage { position: relative; width: 1200px; height: 900px; }
  .card {
    position: absolute;
    width: 600px;
    height: 343px;
    overflow: hidden;
    box-shadow: 0 8px 20px rgba(0,0,0,0.35);
  }
  /* Front side */
  .card-front {
    left: 40px;
    top: 90px;
    background: radial-gradient(ellipse at 50% 35%, #3a3a3a 0%, var(--card-front) 60%);
  }
  .reel-art {
    position: absolute;
    left: 150px;
    top: 20px;
    width: 320px;
    height: 220px;
    border-radius: 50%;
    background: radial-gradient(ellipse at 50% 45%, var(--reel-light) 0%, var(--reel-mid) 40%, var(--reel-dark) 75%, transparent 100%);
    opacity: 0.85;
  }
  .front-brand {
    position: absolute;
    left: 80px;
    bottom: 42px;
    display: flex;
    align-items: center;
    gap: 18px;
  }
  .brand-square {
    width: 58px;
    height: 58px;
    background: var(--ink-light);
    border-radius: 10px;
  }
  .front-brand .brand-name {
    font-weight: 600;
    font-size: 40px;
    letter-spacing: 4px;
    color: var(--ink-silver);
    text-transform: uppercase;
  }
  /* Back side */
  .card-back {
    left: 560px;
    top: 470px;
    background: var(--card-back);
  }
  .reel-ghost {
    position: absolute;
    right: -20px;
    top: 30px;
    width: 360px;
    height: 230px;
    border-radius: 50%;
    background: radial-gradient(ellipse at 50% 50%, rgba(255,255,255,0.07) 0%, rgba(255,255,255,0.03) 55%, transparent 75%);
  }
  .back-brand {
    position: absolute;
    left: 36px;
    top: 78px;
    width: 190px;
    text-align: center;
  }
  .back-brand .brand-square {
    width: 50px;
    height: 50px;
    margin: 0 auto 10px;
  }
  .back-brand .brand-name {
    font-weight: 600;
    font-size: 30px;
    line-height: 1.05;
    letter-spacing: 3px;
    color: var(--accent-red);
    text-transform: uppercase;
  }
  .divider {
    position: absolute;
    left: 248px;
    top: 60px;
    width: 3px;
    height: 150px;
    background: var(--accent-red);
  }
  .tagline {
    position: absolute;
    left: 272px;
    top: 60px;
    font-weight: 800;
    font-size: 22px;
    color: var(--ink-light);
  }
  .contacts {
    position: absolute;
    left: 272px;
    top: 160px;
    font-size: 14px;
    line-height: 1.5;
    color: var(--ink-light);
    list-style: none;
  }
  .contacts li { display: flex; }
  .contacts .label { width: 26px; flex: none; }
</style>
</head>
<body>
<main class="stage">
  <section class="card card-front" aria-label="Card front">
    <div class="reel-art" role="img" aria-label="Silver curling film strip with reflection"></div>
    <div class="front-brand">
      <span class="brand-square" aria-hidden="true"></span>
      <span class="brand-name">Verdo Studios</span>
    </div>
  </section>

  <section class="card card-back" aria-label="Card back">
    <div class="reel-ghost" role="img" aria-label="Faint film strip decoration"></div>
    <div class="back-brand">
      <span class="brand-square" aria-hidden="true"></span>
      <p class="brand-name">Verdo<br>Studios</p>
    </div>
    <div class="divider"></div>
    <p class="tagline">Filmmaking Done Right</p>
    <ul class="contacts">
      <li><span class="label">W:</span><span>www.verdostudios-example.com</span></li>
      <li><span class="label"></span><span>www.facebook.com/verdostudios-example</span></li>
      <li><span class="label">E:</span><span>tomas@verdostudios-example.com</span></li>
      <li><span class="label">S:</span><span>555-318-6092</span></li>
    </ul>
  </section>
</main>
</body>
</html>
```